International freight forwarder experienced in perishable handling needs a web design

We need a website designed that will allow us to capture more customers through the website. We would like a visually appealing design that is not so heavy on text. Our business covers the logistics and freight forwarding industries and we have offices in South America and the USA. Our main customers are importers USA, Europe, Asia and Russia and we currently work almost exclusively with perishable products such as fresh cut flowers, fresh exotics fruits, cacao, fresh fish etc. We would like to convey a fresh, modern approach to freight forwarding focusing on concepts such as - time sensitive, anytime-anywhere delivery, innovation, experience, reliability and confidence. Should include links with Plumetta and Worvanet. Our core solutions include: Core Services
*Air Freight
*Ocean Freight
*Warehousing & Distribution
Our industry solutions cover
*Flowers
*FMCG including, fruits, vegetables
*Live animals
*Automotive
*Consumer Goods
*Industrial
*Oil & Gas
*Pharma
* Event logistics
* Project logistics

Target Market(s)

Importers in Europe, USA, Asia, Middle East and Russia

Number of Pages Required

4 page

Font styles to use
Sans Serif

Colors
a1cd39
606060
000000

Requirements
Must have
• Photos of fresh cut flowers, FMCG such as cacao, fresh fish (packaged for shipping), fresh exotic fruits, pharma products (packaged for shipping), oil and gas etc. Internal customer login access
Nice to have
• Photos of cargo shipping carriers and cargo airline carriers. Features similar to those of following website http://www.brolvacargo.com/eng/main/index.jsp?FromURL=web
Should not have
• Too much text, needs to be visually pleasing

```html
<!DOCTYPE html>
<html lang="en">
<head>
<meta charset="utf-8">
<title>Corvessa Alliance Group</title>
<link rel="stylesheet" href="https://fonts.googleapis.com/css2?family=Jost:wght@600&family=Montserrat:wght@300;400;600&family=PT+Sans:wght@400;700&display=swap">
<style>
  :root {
    --brand-green: #a1cd39;
    --label-green: #8cbf2f;
    --text-grey: #606060;
    --heading-grey: #404040;
    --nav-slate: #3e4a5a;
    --hero-navy: #0f2a6a;
    --night: #2d3440;
    --white: #ffffff;
    --line: #c8c8c8;
  }
  * { margin: 0; padding: 0; box-sizing: border-box; }
  html, body { width: 1200px; height: 1169px; overflow: hidden; }
  body { position: relative; background: var(--night); font-family: "Montserrat", sans-serif; }

  .site-header { position: absolute; left: 0; top: 0; width: 1200px; height: 155px; background: var(--white); }
  .brand { position: absolute; left: 78px; top: 40px; display: flex; align-items: center; gap: 12px; }
  .brand-dot { width: 30px; height: 30px; border-radius: 50%; background: var(--brand-green); }
  .brand-name { font-family: "PT Sans", sans-serif; font-weight: 700; font-size: 32px; color: var(--text-grey); letter-spacing: -0.5px; }
  .utility-nav { position: absolute; right: 97px; top: 50px; font-family: "PT Sans", sans-serif; font-size: 13px; color: var(--nav-slate); }
  .utility-nav span { margin: 0 6px; }
  .main-nav { position: absolute; right: 92px; top: 86px; display: flex; gap: 20px; font-family: "PT Sans", sans-serif; font-size: 19px; color: var(--nav-slate); }

  .hero { position: absolute; left: 0; top: 155px; width: 1200px; height: 399px;
    background: linear-gradient(100deg, #d9d6d0 0%, #bdb4a8 25%, #8a6a55 45%, #5aa0a8 55%, #6b3f7a 70%, #c6b7a2 85%, #e4e1dc 100%); }
  .hero-panel { position: absolute; left: 68px; top: 42px; width: 540px; height: 242px; background: rgba(148, 196, 48, 0.9); padding: 16px 0 0 42px; }
  .hero-services { list-style: none; font-family: "Jost", sans-serif; font-weight: 600; font-size: 35px; line-height: 37px; color: var(--hero-navy); }

  .content { position: absolute; left: 59px; top: 554px; width: 1073px; height: 517px; background: var(--white); }
  .industry { position: absolute; top: 36px; width: 219px; text-align: center; }
  .industry-photo { height: 130px; border: 1px solid var(--line); }
  .industry-name { margin-top: 15px; font-weight: 600; font-size: 17px; letter-spacing: 0.8px; color: var(--label-green); white-space: nowrap; }

  .about { position: absolute; left: 67px; top: 262px; width: 684px; }
  .about h2 { font-weight: 600; font-size: 25px; letter-spacing: 0.6px; color: var(--heading-grey); }
  .about p { margin-top: 10px; font-weight: 400; font-size: 13px; line-height: 21.6px; color: var(--text-grey); }

  .tracker { position: absolute; left: 784px; top: 254px; width: 262px; }
  .tracker h3 { text-align: center; font-weight: 600; font-size: 21px; color: var(--heading-grey); margin-bottom: 8px; font-family: "PT Sans", sans-serif; }
  .tracker-box { position: relative; height: 177px; border: 1px solid var(--line); }
  .tracker-tabs { display: flex; gap: 5px; font-family: "PT Sans", sans-serif; font-size: 15px; }
  .tracker-tab { flex: 1; height: 25px; line-height: 25px; text-align: center; border: 1px solid var(--line); border-top: 0; color: var(--heading-grey); }
  .tracker-tab.is-active { border-bottom-color: transparent; border-left: 0; color: #6f7aa0; }
  .tracker-field { position: absolute; left: 13px; top: 44px; display: flex; align-items: center; gap: 8px; font-family: "PT Sans", sans-serif; font-size: 12px; color: var(--text-grey); }
  .tracker-input { width: 156px; height: 24px; background: #ebebeb; border: 2px solid #cfcfcf; }
  .tracker-button { position: absolute; left: 169px; top: 150px; width: 82px; height: 17px; background: #6b6f80; color: var(--white); font-family: "PT Sans", sans-serif; font-size: 12px; text-align: center; line-height: 17px; }

  .site-footer { position: absolute; left: 102px; top: 1093px; font-family: Arial, sans-serif; font-size: 13px; line-height: 21px; color: var(--white); }
  .social { position: absolute; right: 92px; top: 1104px; display: flex; gap: 14px; font-family: "PT Sans", sans-serif; font-size: 14px; color: #a8adb5; }
</style>
</head>
<body>
  <header class="site-header">
    <div class="brand"><span class="brand-dot"></span><span class="brand-name">Corvessa Alliance</span></div>
    <nav class="utility-nav">Career<span>|</span>Contact</nav>
    <nav class="main-nav"><span>About</span><span>Services</span><span>Network</span><span>Investor Relations</span></nav>
  </header>

  <section class="hero" role="img" aria-label="Air cargo hold with netted pallet of boxed fresh flowers and a worker in a high-visibility vest">
    <div class="hero-panel">
      <ul class="hero-services">
        <li>Air Freight</li>
        <li>Ocean Freight</li>
        <li>Warehousing &amp; Distribution</li>
      </ul>
    </div>
  </section>

  <main class="content">
    <div class="industry" style="left:41px">
      <div class="industry-photo" role="img" aria-label="Bouquet of pink and purple fresh cut flowers" style="background:linear-gradient(135deg,#c45fb0,#e58bc8 50%,#7a4fa8)"></div>
      <div class="industry-name">FRESH CUT FLOWERS</div>
    </div>
    <div class="industry" style="left:294px">
      <div class="industry-photo" role="img" aria-label="Open cacao pod on a wooden table" style="background:linear-gradient(135deg,#5a2e18,#a86a3c 50%,#6b3820)"></div>
      <div class="industry-name">FMCG</div>
    </div>
    <div class="industry" style="left:548px">
      <div class="industry-photo" role="img" aria-label="Fresh fish and prawns on ice" style="background:linear-gradient(135deg,#d9dde0,#8a9aa4 50%,#e7c6b8)"></div>
      <div class="industry-name">FRESH FISH</div>
    </div>
    <div class="industry" style="left:811px">
      <div class="industry-photo" role="img" aria-label="Red gel capsules on a spoon" style="background:radial-gradient(circle at 50% 55%,#d42a1e,#e86a4a 45%,#ffffff 80%)"></div>
      <div class="industry-name">PHARMA PRODUCTS</div>
    </div>

    <section class="about">
      <h2>YOUR TRUSTED PARTNER</h2>
      <p>Lorem ipsum dolor sit amet, consectetuer adipiscing elit, sed diam nonummy nibh euismod tincidunt ut laoreet dolore magna aliquam erat volutpat. Ut wisi enim ad minim veniam, quis nostrud exerci tation ullamcorper suscipit lobortis nisl ut aliquip ex ea commodo consequat. Duis autem vel eum iriure dolor in hendrerit in vulputate velit esse molestie consequat, vel illum dolore eu feugiat nulla facilisis at vero eros et accumsan et iusto odio dignissim qui blandit praesent luptatum zzril delenit augue duis dolore te feugait nulla facilisi. Nam liber tempor cum soluta nobis eleifend option congue nihil imperdiet doming id quod mazim placerat facer possim assum. Typi non habent claritatem insi­tam</p>
    </section>

    <aside class="tracker">
      <h3>Track Order</h3>
      <div class="tracker-box">
        <div class="tracker-tabs"><div class="tracker-tab is-active">Freight</div><div class="tracker-tab">Express</div></div>
        <div class="tracker-field">Track Number <span class="tracker-input"></span></div>
        <div class="tracker-button">Track</div>
      </div>
    </aside>
  </main>

  <footer class="site-footer">
    <div>© 2015 corvessa Alliance</div>
    <div>Home - Site Map – FAQ – Privacy Policy – Terms of Use – Contact Us</div>
  </footer>
  <nav class="social"><span>Plumetta</span><span>Chirpaly</span><span>Feed</span><span>Gravelo</span></nav>
</body>
</html>
```